Gift Card/voucher Design for Beauty Clinic

I need a design for a gift card I Can use in all seasons for my Aesthetic clinic. The Logo is attached. The main colors we use are white and black, we are open for new suggestions to make an friendly yet professional impression. Ideally the gift card/voucher would be foldable.
The inside should contain the following fields:

Für:

Von:

Wert

Gültigkeit

```html
<!DOCTYPE html>
<html lang="de">
<head>
<meta charset="utf-8">
<title>Gutschein – Helena Marwitz Aesthetics</title>
<link rel="stylesheet" href="https://fonts.googleapis.com/css2?family=Arimo&family=Mrs+Saint+Delafield&family=Playfair+Display:wght@500&display=swap">
<style>
  :root {
    --backdrop: #ededed;
    --card: #ffffff;
    --card-edge: #9a9a9a;
    --ink: #111111;
    --brand-navy: #1f2d3a;
    --rule: #555555;
  }
  * { margin: 0; padding: 0; box-sizing: border-box; }
  html, body {
    width: 1200px;
    height: 1199px;
    overflow: hidden;
    background: var(--backdrop);
  }
  .voucher {
    position: absolute;
    left: 127px;
    top: 302px;
    width: 946px;
    height: 596px;
    background: var(--card);
    border: 1px solid var(--card-edge);
  }
  .greeting {
    position: absolute;
    left: 30px;
    top: 60px;
    width: 320px;
    height: 280px;
    font-family: "Mrs Saint Delafield", cursive;
    font-weight: 400;
    color: var(--ink);
    font-size: 122px;
    line-height: 1;
  }
  .greeting__line {
    position: absolute;
    white-space: nowrap;
  }
  .greeting__line--first { left: 52px; top: 12px; }
  .greeting__line--second { left: 8px; top: 118px; }
  .brand-signature {
    position: absolute;
    left: 40px;
    top: 440px;
    width: 258px;
    text-align: center;
    font-family: "Playfair Display", serif;
    font-weight: 500;
    font-size: 16px;
    line-height: 1.5;
    letter-spacing: 1.5px;
    color: var(--brand-navy);
    text-transform: uppercase;
  }
  .fold-divider {
    position: absolute;
    left: 422px;
    top: 65px;
    width: 2px;
    height: 468px;
    background: var(--ink);
  }
  .brand-header {
    position: absolute;
    left: 470px;
    top: 66px;
    width: 450px;
    text-align: center;
    font-family: "Playfair Display", serif;
    font-weight: 500;
    font-size: 33px;
    letter-spacing: 4px;
    color: var(--brand-navy);
    text-transform: uppercase;
  }
  .voucher-fields {
    position: absolute;
    left: 495px;
    top: 156px;
    width: 395px;
    list-style: none;
    font-family: "Arimo", Arial, sans-serif;
    font-size: 28px;
    color: var(--ink);
  }
  .voucher-field {
    display: flex;
    align-items: baseline;
    height: 58px;
    gap: 6px;
  }
  .voucher-field__line {
    flex: 1;
    border-bottom: 1.5px solid var(--rule);
    transform: translateY(-4px);
  }
  .voucher-field--validity { gap: 16px; }
</style>
</head>
<body>
  <main class="voucher">
    <section class="voucher-cover">
      <p class="greeting">
        <span class="greeting__line greeting__line--first">a gift</span>
        <span class="greeting__line greeting__line--second">for you</span>
      </p>
      <p class="brand-signature">Helena Marwitz<br>Aesthetics</p>
    </section>
    <div class="fold-divider"></div>
    <section class="voucher-details">
      <h1 class="brand-header">Helena Marwitz</h1>
      <ul class="voucher-fields">
        <li class="voucher-field"><span>Für:</span><span class="voucher-field__line"></span></li>
        <li class="voucher-field"><span>Von:</span><span class="voucher-field__line"></span></li>
        <li class="voucher-field"><span>Wert</span><span class="voucher-field__line"></span></li>
        <li class="voucher-field voucher-field--validity"><span>Gültigkeit</span><span class="voucher-field__line"></span></li>
      </ul>
    </section>
  </main>
</body>
</html>
```